We are looking to have an icon/button designed for use on a websites.
We want the button to look like a button, or actionable item, and it must include on it, near it or combination with it... ZAP me HERE. This button is our equivalent to "start here." But we need the button to be "iconic" as we will brand off of it. For us ZAP me HERE, written in caps and lower case as shown here, means Prepare to be wow'ed.....your excitement is about to begin. I have attached our company logo and name so you can see our sole image to date.
IMPORTANT: ZAP me HERE should either be neutral in color, metals, grays, etc. or preferably based in GREEN as is our company, BrightLoop.

Target Market(s)

We traditionally target three demographics 18-34, 35-54, 55 plus. For the most part, 54 and younger will be the target market. Internet savy, but looking to be impressed by something different or unique.

Industry/Entity Type

It Company

Colors
acd037

Requirements
Must have
• Must work with the Green of our company name.
Nice to have
• ZAP me HERE is the focus, needs to have a priority in the design
Should not have
• ZAP me HERE needs to be clearly legible. Think relaxed, sleek, efficient, WOW!

```html
<!DOCTYPE html>
<html lang="en">
<head>
<meta charset="utf-8">
<title>ZAP me HERE</title>
<link rel="stylesheet" href="https://fonts.googleapis.com/css2?family=Archivo+Black&family=Barlow:wght@500&display=swap">
<style>
  :root {
    --sky-top: #1c9fda;
    --sky-mid: #5cc4ec;
    --sky-glow: #c6f0fc;
    --ink: #0d1a22;
    --btn-rim: #1f2a22;
    --btn-light: #9fdc6a;
    --btn-mid: #5cb83a;
    --btn-dark: #2f8a22;
    --label: #1e4a1e;
    --label-band: #143214;
    --white: #ffffff;
  }
  * { margin: 0; padding: 0; box-sizing: border-box; }
  html, body { width: 1200px; height: 1200px; overflow: hidden; }
  body {
    position: relative;
    background:
      radial-gradient(ellipse 75% 55% at 50% 95%, var(--sky-glow) 0%, rgba(198,240,252,0) 100%),
      linear-gradient(180deg, var(--sky-top) 0%, var(--sky-mid) 60%, #8fd8f4 100%);
  }
  .intro-copy {
    position: absolute;
    top: 112px;
    left: 40px;
    width: 1120px;
    font-family: "Barlow", sans-serif;
    font-weight: 500;
    font-size: 29px;
    line-height: 39.6px;
    letter-spacing: 0.8px;
    color: var(--ink);
    text-align: center;
    text-transform: uppercase;
  }
  .intro-copy span { display: block; white-space: nowrap; }
  .divider {
    position: absolute;
    top: 682px;
    left: 120px;
    width: 960px;
    height: 4px;
    background: radial-gradient(ellipse at center, rgba(20,80,120,0.35) 0%, rgba(20,80,120,0) 70%);
  }
  .cta-button {
    position: absolute;
    left: 223px;
    top: 770px;
    width: 754px;
    height: 208px;
    border-radius: 22px;
    background: var(--btn-rim);
    padding: 12px;
    box-shadow: 0 14px 24px rgba(0,40,70,0.35);
  }
  .cta-face {
    position: relative;
    width: 100%;
    height: 100%;
    border-radius: 14px;
    background: linear-gradient(180deg, var(--btn-light) 0%, var(--btn-mid) 48%, var(--btn-dark) 52%, var(--btn-mid) 100%);
    display: flex;
    align-items: center;
    justify-content: center;
    overflow: hidden;
  }
  .cta-face::before {
    content: "";
    position: absolute;
    left: 14px; right: 14px; top: 8px;
    height: 42%;
    border-radius: 10px 10px 40px 40px;
    background: linear-gradient(180deg, rgba(255,255,255,0.55), rgba(255,255,255,0.05));
  }
  .cta-label {
    position: relative;
    display: flex;
    align-items: center;
    font-family: "Archivo Black", sans-serif;
    font-size: 108px;
    letter-spacing: -3px;
    color: var(--label);
    line-height: 1;
  }
  .cta-label .small-word {
    font-size: 44px;
    letter-spacing: 0;
    color: var(--white);
    background: var(--label-band);
    padding: 6px 12px;
    margin: 0 4px;
  }
  .pointer-icon {
    position: absolute;
    left: 660px;
    top: 880px;
    width: 270px;
    height: 260px;
  }
</style>
</head>
<body>
  <p class="intro-copy">
    <span>Lorem ipsum dolor sit amet, consectetuer adipiscing elit, sed</span>
    <span>diam nonummy nibh euismod tincidunt ut laoreet dolore</span>
    <span>magna aliquam erat volutpat. Ut wisi enim ad minim veniam,</span>
    <span>quis nostrud exerci tation ullamcorper suscipit lobortis nisl</span>
    <span>ut aliquip ex ea commodo consequat. Duis autem vel eum iriure</span>
    <span>dolor in hendrerit in vulputate velit esse molestie consequat,</span>
    <span>vel illum dolore eu feugiat nulla facilisis at vero eros et</span>
    <span>accumsan et iusto odio dignissim qui blandit praesent lupta-</span>
    <span>tum zzril delenit augue duis dolore te feugait nulla facilisi.</span>
    <span>Nam liber tempor cum soluta nobis eleifend option congue</span>
    <span>nihil imperdiet doming id quod mazim placerat facer possim</span>
    <span>assum. Typi non habent claritatem insitam; est usus legentis in</span>
  </p>

  <div class="divider"></div>

  <div class="cta-button">
    <div class="cta-face">
      <div class="cta-label">
        <span>ZAP</span><span class="small-word">me</span><span>HERE</span>
      </div>
    </div>
  </div>

  <svg class="pointer-icon" viewBox="0 0 110 110" aria-hidden="true">
    <g transform="rotate(-28 55 55)">
      <path d="M38 6 q7 -5 13 1 l0 38 q6 -6 12 0 q7 -6 13 1 q8 -5 13 3 l0 30 q0 14 -9 24 l-32 0 q-8 -10 -20 -24 l-13 -16 q-3 -8 6 -9 q6 0 17 12 z"
            fill="var(--white)" stroke="var(--ink)" stroke-width="4" stroke-linejoin="round"/>
      <path d="M63 46 l0 16 M76 47 l0 15 M51 45 l0 17" stroke="var(--ink)" stroke-width="3" stroke-linecap="round"/>
    </g>
  </svg>
</body>
</html>
```